BrineLeaf Development Studio Website

We'd like to create a brand new website for our company, so we can display our portfolio, our team, and our general approach to the app development work that we do. We've attached the website content + portfolio images for your convenience.

Our company is focused on substance over glamour, so we want our website to represent that mentality. We need something simple, and clean. We're open to both minimalist designs and as well as bolder designs.

Target Market(s)

Businesses: Startups and established companies

Coding

Coded - Design and coding required

Number of Pages Required

2 page

Font styles to use
Sans Serif

Colors
f78f20
faa54b
ffffff

Requirements
Must have
• We'd like this project to incorporate an orange highlight colour (#FFA300), but otherwise be more or less, black and white. If you'd like to also add a primary colour in your design (outside of the orange and grayscale colours), we're happy to explore it!

NOTICE: At the top of the portfolio section, we'd like a full banner highlighted section for Palomatic (a SaaS platform owned and operated by BrineLeaf).
Nice to have
• We want the website design to be more on the clean side, for example, look at the portfolio section from: https://www.quillandtread.co.uk/ (ignore the top banner).

We're also open to exploring bold designs, something like: https://verdakip.net/

```html
<!DOCTYPE html>
<html lang="en">
<head>
<meta charset="utf-8">
<title>BrineLeaf Development Studio — Website</title>
<link href="https://fonts.googleapis.com/css2?family=Roboto:wght@400;500;700&family=Poppins:wght@400;500;600;700&display=swap" rel="stylesheet">
<style>
:root{
  --orange:#f78f20;
  --orange-light:#faa54b;
  --peach:#fde4c8;
  --peach-soft:#fef1e2;
  --ink:#1d1d1d;
  --muted:#4a4a4a;
  --line:#e6e6e6;
  --stage:#f1f1f1;
  --panel:#f6f6f6;
  --white:#ffffff;
  --dash-side:#3b4048;
  --dash-top:#505a68;
  --teal:#1aa9a5;
  --alert:#e5262a;
  --slate:#55606d;
}
*{box-sizing:border-box;margin:0;padding:0}
html,body{width:1200px;height:2285px;overflow:hidden}
body{background:var(--stage);font-family:"Poppins",sans-serif;color:var(--ink)}
.page{position:absolute;background:var(--white);overflow:hidden;box-shadow:0 10px 40px rgba(0,0,0,.08)}
.page--home{left:51px;top:100px;width:536px;height:1874px}
.page--portfolio{left:624px;top:100px;width:527px;height:2133px}
.page > *{position:absolute}
svg.deco{left:0;top:0}
.logo{font-weight:700;font-size:9px;color:var(--ink);display:flex;align-items:center;gap:4px;letter-spacing:.2px}
.logo::before{content:"";width:7px;height:7px;background:var(--orange);display:block}
.nav{font-size:5.6px;color:var(--white);font-weight:500}
.nav span{position:absolute;white-space:nowrap}
.btn-outline{border:1px solid var(--white);color:var(--white);border-radius:8px;font-size:5px;display:flex;align-items:center;justify-content:center;font-weight:500}
.btn-solid{background:var(--white);color:var(--orange);border-radius:7px;font-size:5px;display:flex;align-items:center;justify-content:center;font-weight:600}
.btn-pill{background:var(--orange);color:var(--white);border-radius:7px;font-size:5px;font-weight:600;display:flex;align-items:center;justify-content:center;gap:3px}
.btn-pill::after{content:"";width:4px;height:4px;border-radius:50%;background:var(--white)}
.art{border-radius:40% 45% 40% 50%}
.art--hero{background:radial-gradient(circle at 40% 45%,#fff3e4 0 30%,transparent 31%),linear-gradient(150deg,#fcd3a4,#f78f20)}
.art--about{background:radial-gradient(circle at 55% 55%,#4a4a4a 0 18%,transparent 19%),linear-gradient(135deg,#fde4c8,#f9a850)}
.art--approach{background:radial-gradient(circle at 50% 62%,#3c3c3c 0 16%,transparent 17%),linear-gradient(160deg,#fde4c8,#f7b46c)}
.media--photo{background:linear-gradient(135deg,#7a6352,#2e2a2a);border-radius:3px}
.blob{background:var(--peach)}
.eyebrow{font-size:6.5px;font-weight:500;color:var(--ink)}
.h-section{font-family:"Roboto",sans-serif;font-size:15px;font-weight:400;color:var(--ink)}
.h-project{font-family:"Roboto",sans-serif;font-size:17px;font-weight:400;color:var(--ink)}
.body-text{font-size:5.6px;line-height:1.5;color:var(--muted)}
.body-text b{color:var(--ink);font-weight:600}
.body-text p+p{margin-top:6px}
.arrows{display:flex;gap:10px;color:var(--orange);font-size:10px;line-height:1}
.wordmark{font-size:12px;letter-spacing:2px;color:var(--ink)}

/* dashboard table screen */
.ui{background:var(--white);border:1px solid var(--line);box-shadow:0 4px 12px rgba(0,0,0,.1);overflow:hidden}
.ui > div{position:absolute}
.ui-side{left:0;top:0;bottom:0;width:12%;background:var(--dash-side)}
.ui-side::after{content:"";position:absolute;left:15%;right:15%;top:12px;height:60%;background:repeating-linear-gradient(rgba(255,255,255,.35) 0 1px,transparent 1px 6px)}
.ui-top{left:12%;right:0;top:0;height:7px;background:var(--dash-top)}
.ui-head{left:15%;right:3%;top:10px;height:5px;background:#e1e4e8}
.ui-rows{left:15%;right:3%;top:17px;bottom:5px;background:repeating-linear-gradient(#fff 0 5px,#ececec 5px 6px)}
.ui-marks{left:46%;width:16%;top:17px;bottom:5px;background:repeating-linear-gradient(transparent 0 1.5px,var(--orange) 1.5px 3.5px,transparent 3.5px 6px)}
.ui-text{left:17%;width:24%;top:17px;bottom:5px;background:repeating-linear-gradient(transparent 0 2px,#b9b9b9 2px 3px,transparent 3px 6px)}
.ui-checks{right:5%;width:2%;top:17px;bottom:5px;background:repeating-linear-gradient(transparent 0 1.5px,#3fae5a 1.5px 3.5px,transparent 3.5px 6px)}

/* marketplace screen */
.mk-nav{left:0;top:0;bottom:0;width:10%;background:#fafafa;border-right:1px solid var(--line)}
.mk-nav::after{content:"";position:absolute;left:18%;right:18%;top:14px;height:40%;background:repeating-linear-gradient(#c9c9c9 0 1px,transparent 1px 6px)}
.mk-search{left:12%;width:30%;top:3px;height:5px;border:1px solid var(--line);border-radius:2px}
.mk-list{left:12%;width:50%;top:14px;bottom:6px;background:repeating-linear-gradient(#fff 0 9px,#eeeeee 9px 10px)}
.mk-swatch{left:15%;width:4%;top:16px;bottom:8px;background:repeating-linear-gradient(#2b2b2b 0 6px,transparent 6px 10px)}
.mk-hl{left:12%;width:50%;top:24px;height:9px;background:#fde1dc}
.mk-detail{left:64%;right:3%;top:14px;bottom:6px;border-left:1px solid var(--line)}
.mk-tiles{left:66%;right:5%;top:18px;height:18%;background:linear-gradient(90deg,#4e6b87 0 31%,transparent 31% 34%,#9aa4ae 34% 65%,transparent 65% 68%,#3d5a70 68%)}
.mk-fields{left:66%;right:5%;top:42%;bottom:16%;background:repeating-linear-gradient(transparent 0 6px,#dcdcdc 6px 7px)}
.mk-btn{left:66%;right:5%;bottom:8px;height:5px;background:var(--alert);border-radius:1px}

/* mobile setup screen */
.phone{background:var(--white);box-shadow:0 4px 14px rgba(0,0,0,.15);overflow:hidden}
.phone--back{background:#f3f3f3;border:6px solid #9a9a9a;border-top:none;border-bottom:none}
.phone--back .back-head{position:absolute;left:0;right:0;top:0;height:30px;background:#6bbfbd}
.phone--back .back-temps{position:absolute;left:8px;top:78px;width:20px;font-size:5.5px;color:#777;line-height:19.3px}
.phone .ph-head{position:absolute;left:0;right:0;top:0;height:40px;background:var(--teal);color:#fff;font-size:7px;font-weight:600;padding:20px 10px 0}
.phone .ph-head::before{content:"←";position:absolute;left:10px;top:8px;font-size:7px}
.phone .ph-brand{position:absolute;left:0;right:0;top:56px;text-align:center;font-size:8px;font-weight:700;color:var(--alert)}
.phone .ph-step{position:absolute;left:13px;font-size:5.6px;color:var(--teal);display:flex;align-items:center;gap:6px}
.phone .ph-step i{font-style:normal;width:9px;height:9px;background:var(--teal);color:#fff;font-size:5px;display:flex;align-items:center;justify-content:center}
.phone .ph-rail{position:absolute;left:17px;top:120px;width:1px;height:95px;background:var(--line)}
.phone .ph-note{position:absolute;left:31px;top:126px;font-size:4.6px;color:#777}
.phone .ph-note::before{content:"✓ ";color:var(--teal);font-size:6px}
.phone .ph-input{position:absolute;left:28px;width:86px;top:173px;height:12px;border:1px solid #7fc8e8;font-size:4.4px;color:#888;padding:2px 4px}
.phone .ph-btn{position:absolute;left:28px;top:219px;width:56px;height:12px;background:var(--alert);color:#fff;font-size:4.5px;display:flex;align-items:center;justify-content:center}
.phone .ph-cancel{position:absolute;left:31px;top:263px;font-size:4.8px;color:var(--alert)}
.phone .ph-add{position:absolute;right:17px;top:259px;width:38px;height:12px;background:#e2e2e2;color:#999;font-size:4.6px;display:flex;align-items:center;justify-content:center}

/* orders screen */
.or-side{left:0;top:0;bottom:0;width:14%;background:#f4f7fb;border-right:1px solid var(--line)}
.or-side::after{content:"";position:absolute;left:15%;right:15%;top:14px;height:45%;background:repeating-linear-gradient(#9cc3e4 0 1px,transparent 1px 7px)}
.or-label{font-size:3.8px;color:#666}
.or-cards{left:17%;right:3%;top:10px;height:27%;background:linear-gradient(90deg,#f6f6f6 0 23%,transparent 23% 25.5%,#f6f6f6 25.5% 48.5%,transparent 48.5% 51%,#f6f6f6 51% 74%,transparent 74% 76.5%,#f6f6f6 76.5%)}
.or-table{left:17%;right:3%;background:repeating-linear-gradient(#fff 0 5px,#ededed 5px 6px)}
.or-table--half{right:auto;width:38%}
.or-table--right{left:59%;right:3%}

.card{background:var(--white);border-radius:6px;box-shadow:0 4px 14px rgba(0,0,0,.08);padding:14px 16px 10px}
.card .badge{position:absolute;right:14px;top:9px;width:28px;height:6px;background:#cfe0ef;border-radius:2px}
.card .quote{color:var(--orange);font-weight:700;font-size:12px;line-height:.6;float:left;margin-right:6px;margin-top:2px}
.card p{font-size:5.2px;line-height:1.55;color:var(--muted);margin-top:10px}
.card .name{font-size:5.4px;font-weight:600;margin-top:6px;color:var(--ink)}
.card .stars{color:var(--orange);font-size:6px;letter-spacing:1px;margin-top:6px}
.circle-arrow{width:14px;height:14px;border-radius:50%;border:1px solid var(--orange);color:var(--orange);font-size:8px;display:flex;align-items:center;justify-content:center}
.cta{left:0;width:100%;background:var(--orange);color:var(--white)}
.cta h3{position:absolute;font-family:"Roboto",sans-serif;font-weight:400;font-size:14px}
.cta p{position:absolute;font-size:5.6px;line-height:1.5;width:260px}
.cta .btn-solid{position:absolute;font-size:8px;border-radius:3px}
.footer-col h4{font-size:7px;font-weight:700;color:var(--ink);letter-spacing:.3px}
.footer-col ul{list-style:none;margin-top:6px;font-size:5.2px;font-weight:500;line-height:1.75}
.contact li{display:flex;gap:4px;align-items:flex-start}
.contact li i{width:3px;height:3px;background:var(--ink);border-radius:50%;margin-top:3px;flex:none}
.socials{display:flex;gap:6px;margin-top:9px}
.socials span{width:9px;height:9px;border-radius:50%;background:var(--ink)}
.footer-about{font-size:5.2px;line-height:1.5;color:var(--muted);width:112px}
.copyright{left:0;width:100%;background:var(--peach);font-size:4.8px;text-align:center;display:flex;align-items:center;justify-content:center;color:var(--ink)}
.url{font-size:6.5px;color:var(--ink)}
</style>
</head>
<body>

<section class="page page--home">
  <svg class="deco" width="536" height="310" viewBox="0 0 536 310">
    <path d="M236 0 C244 38 290 36 314 62 C338 108 300 144 330 184 C362 228 450 210 536 244 L536 0 Z" fill="var(--peach)"/>
    <path d="M252 0 C262 30 302 34 324 56 C348 104 316 138 344 176 C372 214 454 198 536 232 L536 0 Z" fill="var(--orange)"/>
    <path d="M0 246 C150 240 250 250 350 270 C430 285 490 290 536 290 L536 298 C470 300 400 292 330 280 C230 262 120 256 0 258 Z" fill="var(--orange)"/>
  </svg>
  <div class="logo" style="left:29px;top:15px">BrineLeaf</div>
  <nav class="nav" style="left:0;top:13px">
    <span style="left:273px">Home</span>
    <span style="left:309px">Who We Are</span>
    <span style="left:365px">Portfolio</span>
    <span style="left:409px">Team</span>
  </nav>
  <div class="btn-outline" style="left:472px;top:10px;width:41px;height:11px">Get Started</div>
  <div class="art art--hero" role="img" aria-label="Illustration of a team building a strategy dashboard with charts" style="left:291px;top:72px;width:222px;height:154px"></div>

  <div class="eyebrow" style="left:27px;top:100px;font-size:8px">Digital Products by Experienced Entrepreneurs</div>
  <h1 style="left:26px;top:113px;font-family:Roboto,sans-serif;font-weight:400;font-size:19.5px;line-height:1.08;width:250px">Where Software Engineering and Business Strategy Collide</h1>
  <div class="btn-pill" style="left:27px;top:184px;width:51px;height:12px">READ MORE</div>

  <div class="art art--about" role="img" aria-label="Illustration of entrepreneurs with a briefcase, lightbulb and trophy" style="left:47px;top:321px;width:231px;height:142px"></div>
  <div class="eyebrow" style="left:322px;top:341px">About Us</div>
  <h2 class="h-section" style="left:322px;top:353px">Who We Are</h2>
  <p class="body-text" style="left:322px;top:376px;width:160px;color:var(--ink);font-size:6.2px">Non-technical entrepreneurs who aspire to bring their ideas to life Businesses looking to implement strategic tech solutions Larger enterprises looking to roll out new initiatives ideas to life Businesses looking to implement strategic tech solutions Larger enterprises looking to roll out new initiatives</p>

  <div class="blob" style="left:352px;top:520px;width:230px;height:200px;border-radius:60% 0 0 50%"></div>
  <div class="eyebrow" style="left:52px;top:554px">Our Work</div>
  <h2 class="h-section" style="left:52px;top:566px">Portfolio</h2>
  <p style="left:52px;top:586px;width:185px;font-family:Roboto,sans-serif;font-size:12px;line-height:1.42;color:#555;font-weight:500"><b style="color:var(--ink);font-weight:500">Description:</b> Secondary Marketplace Solution For Stone Fabricators And Design Professionals</p>
  <div style="left:52px;top:660px;font-size:7px;font-weight:600">Design, Consulting, Web App, Mobile App</div>
  <div class="btn-pill" style="left:52px;top:679px;width:51px;height:12px">SHOW MORE</div>
  <div class="ui" style="left:258px;top:561px;width:170px;height:142px">
    <div class="mk-nav"></div><div class="mk-search"></div><div class="mk-list"></div><div class="mk-hl"></div><div class="mk-swatch"></div>
    <div class="mk-detail"></div><div class="mk-tiles"></div><div class="mk-fields"></div><div class="mk-btn"></div>
  </div>
  <div class="wordmark" style="left:434px;top:682px">Stoneloop</div>
  <div class="arrows" style="left:447px;top:719px"><span>⟵</span><span>⟶</span></div>

  <svg class="deco" style="top:760px" width="536" height="340" viewBox="0 0 536 340">
    <path d="M0 30 C140 0 300 4 420 20 C480 28 520 30 536 26 L536 325 C420 340 300 330 180 335 C100 338 40 332 0 328 Z" fill="var(--panel)"/>
    <path d="M36 100 C60 60 170 60 230 90 C280 120 268 200 240 240 C200 290 100 300 60 270 C20 240 10 150 36 100 Z" fill="var(--peach)"/>
  </svg>
  <h2 class="h-section" style="left:0;width:536px;text-align:center;top:794px">Our Approach</h2>
  <div class="art art--approach" role="img" aria-label="Illustration of a developer coding at a desk surrounded by language tags" style="left:60px;top:842px;width:200px;height:190px;border-radius:8px"></div>
  <div class="body-text" style="left:317px;top:849px;width:172px;font-size:5.4px">
    <p style="color:var(--ink);font-size:6.2px"><b>Focus ;</b> We only play within our realm of excellence</p>
    <p style="margin-top:1px">Our focus is helping you design, launch and evolve your mobile / web technology solutions.</p>
    <p style="color:var(--ink);font-size:6.2px;margin-top:4px"><b>Quality over Quantity ;</b> We engage more deeply in fewer projects</p>
    <p style="margin-top:1px">Our trusted core team is only focused on a handful of projects and we typically work with our clients on an on-going basis to refine and evolve their offering in the market.</p>
    <p style="color:var(--ink);font-size:6.2px;margin-top:4px"><b>Entrepreneurial at Heart ;</b> Operating with a scrappy and multi-disciplinary approach</p>
    <p style="margin-top:1px">We've learned to do more with less, so we can provide top-notch value for your dollar. When working with us, you work directly with the owner-operators and their core team of local experts.</p>
    <p style="color:var(--ink);font-size:6.2px;margin-top:4px"><b>Function over Flash ;</b> Simple, effective execution takes priority over glamour</p>
    <p style="margin-top:1px">Our primary interest is in helping you maximize your key business metrics through technical excellence, sound strategy, and a keen understanding of your end-user.</p>
  </div>

  <div class="blob" style="left:380px;top:1118px;width:180px;height:195px;border-radius:60% 0 0 60%"></div>
  <h2 class="h-section" style="left:73px;top:1120px;font-size:16px">Review</h2>
  <p class="body-text" style="left:74px;top:1143px;width:270px;color:var(--ink)">Lorem ipsum dolor sit amet, consetetur sadipscing elitr, sed diam nonumy eirmod tempor invidunt ut labore et dolore magna aliquyam erat, sed diam voluptua. At vero</p>
  <div class="circle-arrow" style="left:30px;top:1231px">⟵</div>
  <article class="card" style="left:62px;top:1180px;width:176px;height:115px"><span class="badge"></span><p><span class="quote">“</span>Lorem ipsum dolor sit amet, consetetur sadipscing elitr, sed diam nonumy eirmod tempor invidunt ut labore et dolore magna aliquyam erat, sed diam voluptua. At vero eos et accusam et justo duo dolores et ea rebum. Stet clita kasd gubergren, no sea takimata sanctus.</p><div class="name">Milo Fenwick</div><div class="stars">★★★★★</div></article>
  <article class="card" style="left:249px;top:1180px;width:176px;height:115px"><span class="badge"></span><p><span class="quote">“</span>Lorem ipsum dolor sit amet, consetetur sadipscing elitr, sed diam nonumy eirmod tempor invidunt ut labore et dolore magna aliquyam erat, sed diam voluptua. At vero eos et accusam et justo duo dolores et ea rebum. Stet clita kasd gubergren, no sea takimata sanctus.</p><div class="name">Milo Fenwick</div><div class="stars">★★★★★</div></article>
  <article class="card" style="left:436px;top:1180px;width:176px;height:115px"><span class="badge"></span><p><span class="quote">“</span>Lorem ipsum dolor sit amet, consetetur sadipscing elitr, sed diam nonumy eirmod tempor invidunt ut labore et dolore magna aliquyam erat, sed diam voluptua. At vero eos et accusam et justo duo dolores et ea rebum. Stet clita kasd gubergren, no sea takimata sanctus.</p><div class="name">Milo Fenwick</div><div class="stars">★★★★★</div></article>

  <h2 class="h-section" style="left:0;width:536px;text-align:center;top:1405px">Executive Team</h2>
  <p class="body-text" style="left:90px;top:1430px;width:356px;text-align:center;color:var(--ink)">Lorem ipsum dolor sit amet, consetetur sadipscing elitr, sed diam nonumy eirmod tempor invidunt ut labore et dolore magna aliquyam erat, sed diam voluptua. At vero eos et accusam et justo duo</p>
  <div class="media--photo" role="img" aria-label="Portrait photo of the cofounder in a suit" style="left:78px;top:1474px;width:169px;height:111px"></div>
  <div style="left:284px;top:1483px;font-size:8px;font-weight:600">Cofounder ; <span style="font-weight:500;font-size:7px">Darian Kessel, Cofounder</span></div>
  <p class="body-text" style="left:284px;top:1499px;width:178px;font-size:6.5px;color:var(--ink)">Darian is an Engineer, full-stack developer and award-winning entrepreneur. He was recognized and awarded by Sir Alden Marsh for his earlier entrepreneurial work. He is also the founder and technology lead for Palomatic, a SaaS solution recognized by the construction industry throughout North America.</p>
  <div class="arrows" style="left:447px;top:1599px"><span>⟵</span><span>⟶</span></div>

  <div class="cta" style="top:1636px;height:73px">
    <h3 style="left:44px;top:20px">Start Your 14 Day Free Trial</h3>
    <p style="left:44px;top:40px">Lorem ipsum dolor sit amet, consetetur sadipscing elitr, sed diam nonumy eirmod tempor invidunt ut labore et dolore magna aliquyam erat, sed</p>
    <div class="btn-solid" style="left:425px;top:26px;width:67px;height:21px">Get Started</div>
  </div>

  <div class="logo" style="left:68px;top:1760px;font-size:10px">BrineLeaf</div>
  <p class="footer-about" style="left:58px;top:1777px">Lorem ipsum dolor sit amet, consetetur sadipscing elitr, sed diam nonumy eirmod tempor invidunt ut labore et</p>
  <div class="footer-col" style="left:208px;top:1753px"><h4>USEFULL LINKS</h4><ul><li>HOME</li><li>Who We Are</li><li>Team</li><li>Testimonial</li><li>Portfolio</li><li>Approach</li></ul></div>
  <div class="footer-col contact" style="left:307px;top:1753px"><h4>CONTACT US</h4><ul><li><i></i>41 Harbor Lane, Portvale,<br>NY 10288</li><li><i></i>+44(0)20 4812-6630</li><li><i></i>hello@brineleaf.dev</li></ul></div>
  <div class="footer-col" style="left:415px;top:1753px"><h4>SOCIAL LINKS</h4><div class="socials"><span></span><span></span><span></span></div></div>
  <div class="copyright" style="top:1855px;height:19px">© 2021 brineleaf.dev. All Rights</div>
</section>

<section class="page page--portfolio">
  <svg class="deco" width="527" height="270" viewBox="0 0 527 270">
    <path d="M240 0 C250 30 300 30 320 55 C340 90 320 120 350 140 C390 165 460 130 527 125 L527 0 Z" fill="var(--peach)"/>
    <path d="M252 0 C264 24 306 26 330 48 C352 82 334 112 362 130 C398 152 462 120 527 116 L527 0 Z" fill="var(--orange)"/>
    <path d="M0 209 C150 206 260 222 360 240 C430 252 490 256 527 250 L527 258 C480 264 420 262 350 250 C240 232 130 218 0 218 Z" fill="var(--orange)"/>
  </svg>
  <div class="logo" style="left:28px;top:17px">BrineLeaf</div>
  <nav class="nav" style="left:0;top:15px">
    <span style="left:285px">Home</span>
    <span style="left:320px">Who We Are</span>
    <span style="left:376px">Portfolio</span>
    <span style="left:419px">Team</span>
  </nav>
  <div class="btn-solid" style="left:465px;top:13px;width:41px;height:11px">Get Started</div>
  <h1 style="left:0;width:527px;text-align:center;top:114px;font-family:Roboto,sans-serif;font-weight:400;font-size:19px">Our Portfolio</h1>
  <p class="body-text" style="left:93px;top:150px;width:342px;text-align:center;color:var(--ink);font-size:7.2px">Lorem ipsum dolor sit amet, consetetur sadipscing elitr, sed diam nonumy eirmod tempor invidunt ut labore et dolore magna aliquyam erat, sed</p>

  <div class="blob" style="left:0;top:290px;width:250px;height:210px;border-radius:0 55% 50% 0"></div>
  <div class="ui" style="left:21px;top:334px;width:228px;height:133px">
    <div class="ui-side"></div><div class="ui-top"></div><div class="ui-head"></div><div class="ui-rows"></div><div class="ui-text"></div><div class="ui-marks"></div><div class="ui-checks"></div>
  </div>
  <div class="url" style="left:263px;top:326px">Palomatic.com</div>
  <h2 class="h-project" style="left:263px;top:335px">Palomatic</h2>
  <div class="body-text" style="left:263px;top:362px;width:230px;color:var(--ink)">
    <p><b>Overview:</b> BrineLeaf Palomatic is a specialized construction SaaS solution with an established footprint in the North American market.</p>
    <p><b>Background:</b> As a tech entrepreneur and an Engineer who grew up in the construction industry, Darian saw a challenge around the construction tendering process, and created Palomatic to provide a simple, streamlined solution. Five years later and Palomatic has helped construction professionals tender thousands of projects, send out many millions of emails, and support hundreds of construction estimating professionals throughout North America.</p>
    <p>Our niche solution is known for its simplicity, reliability and fair privacy policy, where users own the contact list data that they use within the platform.</p>
  </div>

  <div class="blob" style="left:370px;top:515px;width:170px;height:210px;border-radius:60% 0 0 55%"></div>
  <div class="url" style="left:47px;top:533px">Stoneloop.com</div>
  <h2 class="h-project" style="left:47px;top:542px">Stoneloop</h2>
  <div class="body-text" style="left:47px;top:567px;width:208px;color:var(--ink)">
    <p><b>Background:</b> Stoneloop is a brand-new secondary marketplace that connects stone fabricators with designers and construction professionals in order to maximize the use of stone slab off-cuts. Stoneloop solves a real market need while helping to recycle valuable construction materials and reduce waste.</p>
    <p><b>Challenge:</b> The founder and CEO of Stoneloop is a business-savvy construction entrepreneur who needed a way to bring his vision to reality, by developing the technological assets that would enable Stoneloop to begin executing on their business development and market penetration.</p>
    <p><b>Solution:</b> BrineLeaf consulted with Stoneloop to understand their market, business strategy and end-users, and used that knowledge to design, and build a technical solution for both a mobile and web experience (along with the necessary infrastructure). The first phase of the project will officially be launching in the spring of 2021.</p>
  </div>
  <div class="ui" style="left:278px;top:556px;width:186px;height:153px">
    <div class="mk-nav"></div><div class="mk-search"></div><div class="mk-list"></div><div class="mk-hl"></div><div class="mk-swatch"></div>
    <div class="mk-detail"></div><div class="mk-tiles"></div><div class="mk-fields"></div><div class="mk-btn"></div>
  </div>

  <div class="blob" style="left:0;top:790px;width:150px;height:250px;border-radius:0 50% 50% 0;background:var(--peach-soft)"></div>
  <div class="phone phone--back" style="left:61px;top:805px;width:127px;height:275px">
    <div class="back-head"></div>
    <div class="back-temps">37.5°<br>37.0°<br>36.5°<br>36.0°<br>35.5°<br>35.0°<br>34.5°<br>34.0°</div>
  </div>
  <div class="phone" style="left:103px;top:773px;width:135px;height:288px">
    <div class="ph-head">Add New Device</div>
    <div class="ph-brand">Tempra</div>
    <div class="ph-rail"></div>
    <div class="ph-step" style="top:106px"><i>1</i>Connect to Device</div>
    <div class="ph-note">Device connected!</div>
    <div class="ph-step" style="top:154px"><i>2</i>Name Your Device</div>
    <div class="ph-input">Main Lobby</div>
    <div class="ph-step" style="top:201px"><i>3</i>Set Up Device WiFi</div>
    <div class="ph-btn">Set Up WiFi</div>
    <div class="ph-cancel">Cancel</div>
    <div class="ph-add">Add Device</div>
  </div>
  <div class="url" style="left:289px;top:816px">Tempra.com</div>
  <h2 class="h-project" style="left:289px;top:825px">Tempra</h2>
  <div class="body-text" style="left:289px;top:850px;width:204px;color:var(--ink)">
    <p><b>Background:</b> The Tempra device is an innovative temperature screening device created by the Veyra Health Inc. in response to the recent pandemic. Tempra helps to create a safer environment for businesses by performing an automated hands-free temperature screening for all incoming individuals.</p>
    <p><b>Challenge:</b> Tempra needed a simple and streamlined process to allow users to set up and customize each of their devices. Veyra Health Inc. also needed an comprehensive IT infrastructure to support the large amounts of data that would be streaming to and from a large network of Tempra devices on a regular basis.</p>
    <p><b>Solution:</b> The BrineLeaf team worked with Veyra Health Inc. to design and develop a mobile app for iOS and Android that communicates with the devices through a Bluetooth Low Energy connection in order to facilitate the setup of Tempra devices including connecting devices to WiFi and defining temperature threshold and notification settings as well as monitor the ongoing activity and status of the devices. Furthermore, BrineLeaf set up a robust and secure backend architecture to support the ever growing number of Tempra devices.</p>
  </div>

  <div class="blob" style="left:330px;top:1140px;width:210px;height:190px;border-radius:55% 0 0 50%"></div>
  <div class="url" style="left:41px;top:1146px">Crateway.com</div>
  <h2 class="h-project" style="left:41px;top:1155px">Crateway</h2>
  <div class="body-text" style="left:41px;top:1180px;width:224px;color:var(--ink)">
    <p><b>Background:</b> Crateway is a fast-growing startup company in the storage and logistics sector. They are going above and beyond conventional warehousing and storage lockers to provide a fully managed solution where business assets are catalogued, stored, and transported based on client needs with innovative technology deeply integrated into the process.</p>
    <p><b>Challenge:</b> As Crateway was succeeding in the growth of their client base, managing the ever-growing inventory of items and the expanding use-cases from clients became a challenge with regards to operations and technology. Their existing technology and the corresponding processes started to become suboptimal for responding to the evolving market demands.</p>
    <p><b>Solution:</b> BrineLeaf works with Crateway to understand their business, review their existing technology and learn about their current processes. By gaining a genuine understanding of the nuances of their business, BrineLeaf provides on-going updates to restructure and enhance the existing technologies. The main objective of these changes is to enhance operational efficiency and accuracy, and meet the ever-evolving requirements of new and existing Crateway clients</p>
  </div>
  <div class="ui" style="left:278px;top:1205px;width:232px;height:129px">
    <div class="or-side"></div>
    <div class="or-label" style="left:17%;top:3px">Create an Order</div>
    <div class="or-cards"></div>
    <div class="or-label" style="left:17%;top:47px">Current Orders</div>
    <div class="or-table" style="top:53px;height:24px"></div>
    <div class="or-label" style="left:17%;top:83px">New Items</div>
    <div class="or-label" style="left:59%;top:83px">Items for Review</div>
    <div class="or-table or-table--half" style="top:89px;height:30px"></div>
    <div class="or-table or-table--right" style="top:89px;height:30px"></div>
  </div>

  <div class="blob" style="left:0;top:1400px;width:265px;height:215px;border-radius:0 55% 55% 0"></div>
  <div class="ui" style="left:18px;top:1437px;width:252px;height:142px">
    <div class="ui-side"></div><div class="ui-top"></div><div class="ui-head"></div><div class="ui-rows"></div><div class="ui-text"></div><div class="ui-marks"></div><div class="ui-checks"></div>
  </div>
  <div class="url" style="left:289px;top:1418px">Tempra.com</div>
  <h2 class="h-project" style="left:289px;top:1427px">Tempra</h2>
  <div class="body-text" style="left:289px;top:1452px;width:204px;color:var(--ink)">
    <p><b>Background:</b> Lumen Pulse is a cutting-edge neuroscience based music composition service. Through neuroscientific principles and empirical research, Lumen Pulse creates auditory experiences to enhance states of focus, sleep and relaxation.</p>
    <p><b>Challenge:</b> Lumen Pulse is a young company with a very unique offering in the market. The CEO is a science-oriented inventor, who is looking to present his company and their accomplishments in a concise fashion and to find product-market fit.</p>
    <p><b>Solution:</b> BrineLeaf began consulting with Lumen Pulse in order to understand their offering, the scientific backing and subsequently begin market research into the space, and start designing a product roadmap for promising directions.</p>
  </div>

  <div class="blob" style="left:370px;top:1673px;width:170px;height:205px;border-radius:60% 0 0 60%"></div>
  <h2 class="h-section" style="left:72px;top:1675px;font-size:16px">Review</h2>
  <p class="body-text" style="left:73px;top:1698px;width:270px;color:var(--ink)">Lorem ipsum dolor sit amet, consetetur sadipscing elitr, sed diam nonumy eirmod tempor invidunt ut labore et dolore magna aliquyam erat, sed diam voluptua. At vero</p>
  <div class="circle-arrow" style="left:30px;top:1786px">⟵</div>
  <article class="card" style="left:61px;top:1734px;width:173px;height:114px"><span class="badge"></span><p><span class="quote">“</span>Lorem ipsum dolor sit amet, consetetur sadipscing elitr, sed diam nonumy eirmod tempor invidunt ut labore et dolore magna aliquyam erat, sed diam voluptua. At vero eos et accusam et justo duo dolores et ea rebum. Stet clita kasd gubergren, no sea takimata sanctus.</p><div class="name">Milo Fenwick</div><div class="stars">★★★★★</div></article>
  <article class="card" style="left:244px;top:1734px;width:173px;height:114px"><span class="badge"></span><p><span class="quote">“</span>Lorem ipsum dolor sit amet, consetetur sadipscing elitr, sed diam nonumy eirmod tempor invidunt ut labore et dolore magna aliquyam erat, sed diam voluptua. At vero eos et accusam et justo duo dolores et ea rebum. Stet clita kasd gubergren, no sea takimata sanctus.</p><div class="name">Milo Fenwick</div><div class="stars">★★★★★</div></article>
  <article class="card" style="left:426px;top:1734px;width:173px;height:114px"><span class="badge"></span><p><span class="quote">“</span>Lorem ipsum dolor sit amet, consetetur sadipscing elitr, sed diam nonumy eirmod tempor invidunt ut labore et dolore magna aliquyam erat, sed diam voluptua. At vero eos et accusam et justo duo dolores et ea rebum. Stet clita kasd gubergren, no sea takimata sanctus.</p><div class="name">Milo Fenwick</div><div class="stars">★★★★★</div></article>

  <div class="cta" style="top:1902px;height:71px">
    <h3 style="left:43px;top:17px">Start Your 14 Day Free Trial</h3>
    <p style="left:43px;top:38px">Lorem ipsum dolor sit amet, consetetur sadipscing elitr, sed diam nonumy eirmod tempor invidunt ut labore et dolore magna aliquyam erat, sed</p>
    <div class="btn-solid" style="left:418px;top:25px;width:66px;height:21px">Get Started</div>
  </div>

  <div class="logo" style="left:67px;top:2023px;font-size:10px">BrineLeaf</div>
  <p class="footer-about" style="left:57px;top:2040px">Lorem ipsum dolor sit amet, consetetur sadipscing elitr, sed diam nonumy eirmod tempor invidunt ut labore et</p>
  <div class="footer-col" style="left:205px;top:2016px"><h4>USEFULL LINKS</h4><ul><li>HOME</li><li>Who We Are</li><li>Team</li><li>Testimonial</li><li>Portfolio</li><li>Approach</li></ul></div>
  <div class="footer-col contact" style="left:302px;top:2016px"><h4>CONTACT US</h4><ul><li><i></i>41 Harbor Lane, Portvale,<br>NY 10288</li><li><i></i>+44(0)20 4812-6630</li><li><i></i>hello@brineleaf.dev</li></ul></div>
  <div class="footer-col" style="left:408px;top:2016px"><h4>SOCIAL LINKS</h4><div class="socials"><span></span><span></span><span></span></div></div>
  <div class="copyright" style="top:2117px;height:16px">© 2021 brineleaf.dev. All Rights</div>
</section>

</body>
</html>
```